BRAVO (Bright Regional Applied Vector Operations) Letter Head Design Project

Company Name: BRAVO (Bright Regional Applied Vector Operations) MFZ.
Office Address: Office No 718, Saffron Crest Block, Palmera Garden Quarter, Dubai, U.A.E
Company line of business:
1) Currently we have a POS solution for retail outlets like duty free shops, supermarkets, department stores etc... The solution is deployed in Harbourline Travel Retail on 350 POS and in Corniche Gate Travel Retail on 100 POS. So our main line of business is the deployment of this solution in retail outlets locally or regionally. We have already deployed the solution in India and Australia.
2) Integration of other third party POS systems with an online credit authorization netwotk in the UAE. This will enable POS applications to connect directly to the acquiring banks without needing an EFT terminal like Paxomat or Tallyrex. The credit card payment is completed at the POS.
3) Other solutions that are targeting retail outlets like mobile POS, queue busting solutions, stock taking solutions using hand held devices, transaction capture systems, etc...
4) Other IT services like support of call center solutions from Bluegrove Systems and development of new solutions as per customer requirements.
We need a letter head design for the company. We don't have any specific requirements in mind and we prefer to leave it up to the designers to come up with creative designs that will not be limited by any guidelines.
Updates
I have just uploaded all the files I received from my company logo designer. Please review and let me know if you need anything else. .
Dear All,
I have received very nice designs and I thank you for all the hard work you have put so far. I would like the letter head to have all the following company details:
Office Address: Office No 718, Saffron Crest Block, MFZ, Dubai UAE
P.O.Box: 58316 Dubai UAE
Tel Number:+971-4-5817730
Fax Number::+971-4-5817731
Website:www.bravomfz.ae
I would also like to represent the company details as a QRCode somewhere on the page, probably next to the company details if possible (as a trial).
In case you have included a butterfly in the middle of the page as part of your design, I prefer that it doesn't include any colors as colors might make reading the text on the page more difficult.
I don't want to have too many butterflies on the page. 2 are more than enough.
Can you also include a design for the continuation pages?
Thank you in advance and I look forward to receiving your creative designs.
Regards
Samir Odeyra

```html
<!DOCTYPE html>
<html lang="en">
<head>
<meta charset="utf-8">
<title>BRAVO Letterhead – First and Continuation Pages</title>
<link href="https://fonts.googleapis.com/css2?family=Open+Sans:wght@400;600&display=swap" rel="stylesheet">
<style>
  :root {
    --backdrop: #a27d24;
    --paper: #ffffff;
    --ink: #1a1a1a;
    --rule: #111111;
    --accent: #2aa3d8;
    --mark: #1f6fc4;
  }
  * { margin: 0; padding: 0; box-sizing: border-box; }
  html, body {
    width: 1200px;
    height: 787px;
    overflow: hidden;
    background: var(--backdrop);
    font-family: "Open Sans", Arial, sans-serif;
    color: var(--ink);
  }
  .sheet {
    position: absolute;
    width: 524px;
    height: 678px;
    background: var(--paper);
  }
  .sheet--first { left: 30px; top: 40px; }
  .sheet--continuation { left: 621px; top: 39px; }

  .rule {
    position: absolute;
    height: 2px;
    background: var(--rule);
  }

  .brand {
    position: absolute;
    display: flex;
    align-items: center;
    gap: 8px;
  }
  .brand__dot {
    width: 18px;
    height: 18px;
    border-radius: 50%;
    background: var(--mark);
  }
  .brand__name {
    font-size: 30px;
    font-weight: 600;
    letter-spacing: 2px;
    line-height: 1;
    color: var(--ink);
  }

  /* first page */
  .sheet--first .rule--left { left: 0; top: 60px; width: 48px; }
  .sheet--first .rule--right { left: 232px; top: 60px; width: 292px; }
  .sheet--first .brand { left: 60px; top: 44px; }

  .address {
    position: absolute;
    font-size: 8px;
    line-height: 12px;
  }
  .sheet--first .address {
    right: 38px;
    top: 30px;
    text-align: right;
  }

  .contact-list {
    position: absolute;
    right: 38px;
    top: 74px;
    list-style: none;
    font-size: 8px;
    line-height: 11px;
    text-align: right;
  }
  .contact-list li {
    display: flex;
    justify-content: flex-end;
    align-items: center;
    gap: 4px;
  }

  .icon {
    width: 7px;
    height: 7px;
    flex: none;
  }
  .icon circle { fill: var(--accent); }
  .icon path { fill: none; stroke: #ffffff; stroke-width: 1.2; stroke-linecap: round; }

  /* continuation page */
  .sheet--continuation .rule--left { left: 0; top: 45px; width: 170px; }
  .sheet--continuation .rule--right { left: 358px; top: 45px; width: 166px; }
  .sheet--continuation .brand { left: 186px; top: 29px; }
  .sheet--continuation .address {
    left: 0;
    right: 0;
    top: 78px;
    text-align: center;
  }
  .contact-row {
    position: absolute;
    left: 0;
    right: 0;
    top: 94px;
    display: flex;
    justify-content: center;
    gap: 14px;
    list-style: none;
    font-size: 8px;
    line-height: 12px;
  }
  .contact-row li {
    display: flex;
    align-items: center;
    gap: 2px;
  }
</style>
</head>
<body>

<section class="sheet sheet--first" aria-label="Letterhead first page">
  <div class="rule rule--left"></div>
  <div class="brand">
    <span class="brand__dot"></span>
    <span class="brand__name">BRAVO</span>
  </div>
  <div class="rule rule--right"></div>

  <p class="address">Office No 718, Saffron Crest Block,<br>Palmera Garden Quarter, Dubai, U.A.E</p>

  <ul class="contact-list">
    <li>123-456-7890
      <svg class="icon" viewBox="0 0 10 10"><circle cx="5" cy="5" r="5"/><path d="M3.3 2.8 Q3.3 6.7 7.2 6.7"/></svg>
    </li>
    <li>123-456-7890
      <svg class="icon" viewBox="0 0 10 10"><circle cx="5" cy="5" r="5"/><path d="M3 4.2 H7 M3 6 H7"/></svg>
    </li>
    <li>hello@bravomfz.ae
      <svg class="icon" viewBox="0 0 10 10"><circle cx="5" cy="5" r="5"/><path d="M2.8 3.5 H7.2 V6.5 H2.8 Z M2.8 3.5 L5 5.2 L7.2 3.5"/></svg>
    </li>
    <li>www.bravomfz.ae
      <svg class="icon" viewBox="0 0 10 10"><circle cx="5" cy="5" r="5"/><path d="M2.5 5 H7.5 M5 2.5 Q3.4 5 5 7.5 Q6.6 5 5 2.5"/></svg>
    </li>
  </ul>
</section>

<section class="sheet sheet--continuation" aria-label="Letterhead continuation page">
  <div class="rule rule--left"></div>
  <div class="brand">
    <span class="brand__dot"></span>
    <span class="brand__name">BRAVO</span>
  </div>
  <div class="rule rule--right"></div>

  <p class="address">Office No 718, Saffron Crest Block, Palmera Garden Quarter, Dubai, U.A.E</p>

  <ul class="contact-row">
    <li><svg class="icon" viewBox="0 0 10 10"><circle cx="5" cy="5" r="5"/><path d="M3.3 2.8 Q3.3 6.7 7.2 6.7"/></svg>123-456-7890</li>
    <li><svg class="icon" viewBox="0 0 10 10"><circle cx="5" cy="5" r="5"/><path d="M3 4.2 H7 M3 6 H7"/></svg>123-456-7890</li>
    <li><svg class="icon" viewBox="0 0 10 10"><circle cx="5" cy="5" r="5"/><path d="M2.8 3.5 H7.2 V6.5 H2.8 Z M2.8 3.5 L5 5.2 L7.2 3.5"/></svg>hello@bravomfz.ae</li>
    <li><svg class="icon" viewBox="0 0 10 10"><circle cx="5" cy="5" r="5"/><path d="M2.5 5 H7.5 M5 2.5 Q3.4 5 5 7.5 Q6.6 5 5 2.5"/></svg>www.bravomfz.ae</li>
  </ul>
</section>

</body>
</html>
```